Rebrand/migrate of website to Wordpress

Rebrand/transfer of php website to new wordpress website using the Noxel theme. Dial4LessLines.com is being rebranded to Quorvix and therefore we are looking to simplify the current layout to match competitors sites and be mobile device friendly.
The new site will need to show services in a clear uncluttered way with more emphasis on the service rather than large amounts of text. See attachment B1 for example.
Competitors sites are kx.com , ringmoor.co.uk, zelwire.com
Updates

As I have had a few request from designers to extend the deadline. I have requested Pixel Harbor to extend to Tuesday 3rd April 2018

Target Market(s)

UK Home phone and small business customers

Industry/Entity Type

Telecom

Coding

Coded - Design and coding required

Number of Pages Required

5+ page

Colors

Designer to choose colors to be used in the design.

Requirements
Must have
• 1. Use Noxel wordpress theme that will be supplied.
• 2. Combine the best layouts where possible as used by competitors but in a unique way.
• 3. Horizontal bar should be in white so that it can layer over banner as per file A1.
• 4. Simplify current layout to match competitors see attached file B1.
• 5. Integrate Tallbranch - Tallbranch Leads Web / web form to capture interested customers - name, Company name, Telephone number, email address.
Should not have
• Colour scheme that is the same as our competitors RingMoor, KX, Halden, Vexa Net

```html
<!DOCTYPE html>
<html lang="en">
<head>
<meta charset="utf-8">
<title>Quorvix – Home Phone &amp; Business Calls</title>
<link href="https://fonts.googleapis.com/css2?family=Nunito:wght@400;600;700&display=swap" rel="stylesheet">
<style>
  :root {
    --green: #1a9350;
    --green-dark: #127a3f;
    --red: #e0112b;
    --magenta: #c8135f;
    --navy: #1e3a8a;
    --ink: #222222;
    --muted: #6b6b6b;
    --line: #d6d6d6;
    --panel: #f4f4f4;
    --white: #ffffff;
  }
  * { box-sizing: border-box; margin: 0; padding: 0; }
  html, body { width: 1200px; height: 3056px; overflow: hidden; }
  body { font-family: "Nunito", Arial, sans-serif; color: var(--ink); background: var(--white); position: relative; }
  .abs { position: absolute; }
  .btn { position: absolute; display: flex; align-items: center; justify-content: center; color: var(--white); font-size: 14px; font-weight: 600; }

  /* Header */
  .site-header { position: absolute; top: 0; left: 0; width: 1200px; height: 70px; background: var(--white); z-index: 5; box-shadow: 0 1px 3px rgba(0,0,0,.08); }
  .brand { position: absolute; font-size: 32px; font-weight: 600; color: var(--ink); letter-spacing: .5px; line-height: 1; }
  .site-header .brand { left: 126px; top: 17px; }
  .main-nav a { position: absolute; top: 26px; font-size: 13px; color: var(--ink); text-decoration: none; }

  /* Hero */
  .hero { position: absolute; top: 0; left: 0; width: 1200px; height: 530px; background: linear-gradient(90deg, #eeeeee 0%, #e4e4e4 60%, #dcdcdc 100%); overflow: hidden; }
  .hero-photo { position: absolute; left: 733px; top: 0; width: 467px; height: 530px; background: linear-gradient(160deg, #d9d4cf 0%, #c9c3bc 50%, #e6e3df 100%); }
  .hero-title { left: 67px; top: 198px; font-size: 36px; font-weight: 400; letter-spacing: 1px; }
  .hero-text { left: 67px; top: 248px; width: 360px; font-size: 13px; line-height: 19px; }
  .hero .btn { left: 69px; top: 300px; width: 149px; height: 38px; background: var(--green); }
  .dots { position: absolute; left: 570px; top: 468px; display: flex; gap: 9px; }
  .dots span { width: 8px; height: 8px; border-radius: 50%; background: #9a9a9a; }
  .dots span.on { background: var(--green); }

  /* Icon circles */
  .icon-circle { position: absolute; width: 78px; height: 78px; border-radius: 50%; background: var(--green); display: flex; align-items: center; justify-content: center; }
  .icon-circle svg { width: 36px; height: 36px; }

  /* Services */
  .service { position: absolute; width: 320px; text-align: center; }
  .service h3 { font-size: 18px; font-weight: 600; margin-bottom: 22px; }
  .service p { font-size: 12.5px; color: var(--muted); line-height: 19px; }

  /* Plans */
  .plans { position: absolute; top: 851px; left: 0; width: 1200px; height: 762px; background: var(--panel); }
  .section-title { position: absolute; left: 0; width: 1200px; text-align: center; font-size: 36px; font-weight: 400; }
  .section-sub { position: absolute; left: 0; width: 1200px; text-align: center; font-size: 13px; color: var(--muted); }
  .plan { position: absolute; top: 157px; width: 336px; height: 510px; background: var(--white); text-align: center; }
  .plan h3 { margin-top: 30px; font-size: 24px; font-weight: 400; }
  .plan h4 { margin-top: 8px; font-size: 18px; font-weight: 400; }
  .plan .desc { margin: 14px auto 0; width: 240px; font-size: 14px; line-height: 20px; color: var(--muted); }
  .plan .price { margin-top: 4px; font-size: 23px; color: var(--green); }
  .rates { position: absolute; left: 20px; top: 216px; width: 296px; height: 194px; border: 1px solid #e6e6e6; border-radius: 16px; padding: 32px 22px 0 22px; text-align: left; }
  .rates .row { display: flex; justify-content: space-between; font-size: 14px; height: 30.5px; }
  .rates .row span:last-child { width: 92px; }
  .plan .btn { left: 93px; top: 438px; width: 150px; height: 41px; }

  /* Contact */
  .contact-field { position: absolute; width: 337px; height: 30px; border-bottom: 1px solid var(--line); font-size: 14px; padding-left: 16px; }
  .contact .btn { left: 525px; top: 1978px; width: 149px; height: 41px; background: var(--green); }

  /* Why choose */
  .why { position: absolute; top: 2078px; left: 0; width: 1200px; height: 564px; background: var(--panel); }
  .feature-title { position: absolute; width: 260px; text-align: center; font-size: 18px; }
  .ticks { position: absolute; width: 260px; list-style: none; font-size: 12px; line-height: 18px; color: #333; }
  .ticks li { position: relative; padding-left: 16px; margin-bottom: 18px; min-height: 18px; }
  .ticks li::before { content: ""; position: absolute; left: 1px; top: 6px; width: 5px; height: 5px; border-right: 1.5px solid #333; border-top: 1.5px solid #333; transform: rotate(45deg); }

  /* Call-to-action cards */
  .cta { position: absolute; top: 2689px; width: 428px; height: 208px; border-radius: 16px; text-align: center; color: var(--white); overflow: hidden; }
  .cta.faq { left: 159px; background: linear-gradient(135deg, #e8202f 0%, #c8101f 100%); }
  .cta.mobile { left: 611px; background: linear-gradient(135deg, #22a55b 0%, #137a3f 100%); }
  .cta h3 { margin-top: 30px; font-size: 24px; font-weight: 400; }
  .cta p { margin: 8px auto 0; width: 340px; font-size: 12px; line-height: 18px; }
  .cta .btn { left: 139px; top: 147px; width: 150px; height: 40px; }

  /* Footer */
  .site-footer { position: absolute; top: 2943px; left: 0; width: 1200px; height: 113px; background: var(--panel); }
  .site-footer .brand { left: 55px; top: 42px; }
  .footer-nav a { position: absolute; top: 50px; font-size: 13px; color: var(--ink); text-decoration: none; }
  .copyright { position: absolute; right: 49px; top: 50px; font-size: 12.5px; }
</style>
</head>
<body>

<section class="hero">
  <div class="hero-photo" role="img" aria-label="Photo of a smiling woman holding a mobile phone"></div>
  <h1 class="abs hero-title">QUORVIX</h1>
  <p class="abs hero-text">Make cheap local,national and international unlimites phone calls to your friends famiy and more with our great calling plans</p>
  <a class="btn">Learn More</a>
  <div class="dots"><span class="on"></span><span></span><span></span><span></span></div>
</section>

<header class="site-header">
  <div class="brand">Quorvix</div>
  <nav class="main-nav">
    <a style="left:693px">Home</a>
    <a style="left:777px">About Us</a>
    <a style="left:880px">Residential</a>
    <a style="left:992px">Support</a>
    <a style="left:1087px">My Account</a>
  </nav>
</header>

<section class="services">
  <div class="icon-circle" style="left:193px;top:603px">
    <svg viewBox="0 0 36 36" fill="none" stroke="#fff" stroke-width="2"><rect x="8" y="6" width="20" height="24" rx="1"/><path d="M13 25v-6M18 25v-11M23 25v-8"/></svg>
  </div>
  <div class="service" style="left:72px;top:690px">
    <h3>Business</h3>
    <p>Sed ut perspiciatis unde omnis iste natus error sit voluptatem accusantium doloremque laudantium, totam rem aperiam, eaque ipsa q</p>
  </div>

  <div class="icon-circle" style="left:560px;top:603px">
    <svg viewBox="0 0 36 36" fill="none" stroke="#fff" stroke-width="2"><rect x="9" y="5" width="18" height="26"/><path d="M13 10h3M20 10h3M13 15h3M20 15h3M13 20h3M20 20h3M16 31v-5h4v5"/></svg>
  </div>
  <div class="service" style="left:439px;top:690px">
    <h3>Residential</h3>
    <p>Sed ut perspiciatis unde omnis iste natus error sit voluptatem accusantium doloremque laudantium, totam rem aperiam, eaque ipsa</p>
  </div>

  <div class="icon-circle" style="left:941px;top:603px">
    <svg viewBox="0 0 36 36" fill="none" stroke="#fff" stroke-width="2.5"><circle cx="18" cy="18" r="12"/><circle cx="18" cy="18" r="5"/><path d="M10 10l4 4M26 10l-4 4M10 26l4-4M26 26l-4-4"/></svg>
  </div>
  <div class="service" style="left:820px;top:690px">
    <h3>Support</h3>
    <p>Sed ut perspiciatis unde omnis iste natus error sit voluptatem accusantium doloremque laudantium, totam rem aperiam, eaque ipsa</p>
  </div>
</section>

<section class="plans">
  <h2 class="section-title" style="top:62px">Phone Plans</h2>
  <p class="section-sub" style="top:110px">Make Cheaper Call Now!</p>

  <article class="plan" style="left:69px">
    <h3 style="color:var(--navy)">Plan A</h3>
    <h4>Home Saver</h4>
    <p class="desc">Unlimited local &amp; National evening &amp; weekend calls for just</p>
    <p class="price">£2.99/Month</p>
    <div class="rates">
      <div class="row"><span>Landline</span><span>3.5p/min</span></div>
      <div class="row"><span>Mobiles</span><span>10p/min</span></div>
      <div class="row"><span>0845&amp;0870</span><span>Free</span></div>
      <div class="row"><span>International</span><span>From 1p/min</span></div>
    </div>
    <a class="btn" style="background:var(--navy)">Find Out More</a>
  </article>

  <article class="plan" style="left:434px">
    <h3 style="color:var(--red)">Plan B</h3>
    <h4>Home Saver Anytime</h4>
    <p class="desc">Unlimited local &amp; National evening &amp; weekend calls for just</p>
    <p class="price">£9.99/Month</p>
    <div class="rates">
      <div class="row"><span>Landline</span><span>3.5p/min</span></div>
      <div class="row"><span>Mobiles</span><span>10p/min</span></div>
      <div class="row"><span>0845&amp;0870</span><span>Free</span></div>
      <div class="row"><span>International</span><span>From 1p/min</span></div>
    </div>
    <a class="btn" style="background:var(--red)">Find Out More</a>
  </article>

  <article class="plan" style="left:798px">
    <h3 style="color:var(--magenta)">Plan C</h3>
    <h4>Home Saver International</h4>
    <p class="desc">Unlimited local &amp; National evening &amp; weekend calls for just</p>
    <p class="price">£14.99/Month</p>
    <div class="rates">
      <div class="row"><span>Landline</span><span>3.5p/min</span></div>
      <div class="row"><span>Mobiles</span><span>10p/min</span></div>
      <div class="row"><span>0845&amp;0870</span><span>Free</span></div>
      <div class="row"><span>International</span><span>From 1p/min</span></div>
    </div>
    <a class="btn" style="background:var(--magenta)">Find Out More</a>
  </article>
</section>

<section class="contact">
  <h2 class="section-title" style="top:1688px">Contact Us</h2>
  <p class="section-sub" style="top:1738px;font-size:12px">Sed ut perspiciatis unde omnis iste natus error sit</p>
  <div class="contact-field" style="left:250px;top:1818px">Name</div>
  <div class="contact-field" style="left:611px;top:1818px">Company Name</div>
  <div class="contact-field" style="left:250px;top:1894px">Telephone Number</div>
  <div class="contact-field" style="left:611px;top:1894px">E-Mail Addresss</div>
  <a class="btn">Submit</a>
</section>

<section class="why">
  <h2 class="section-title" style="top:62px">Why Choose Quorvix?</h2>

  <div class="icon-circle" style="left:152px;top:169px">
    <svg viewBox="0 0 36 36" fill="none" stroke="#fff" stroke-width="2"><path d="M6 16c0-6 5-10 12-10s12 4 12 10-5 10-12 10c-2 0-3 0-5-1l-6 3 2-5c-2-2-3-4-3-7z"/><path d="M13 16h10"/></svg>
  </div>
  <div class="icon-circle" style="left:429px;top:169px">
    <svg viewBox="0 0 36 36" fill="none" stroke="#fff" stroke-width="2"><rect x="6" y="11" width="24" height="17" rx="2"/><path d="M9 11l14-5 2 5"/><rect x="22" y="17" width="8" height="5"/></svg>
  </div>
  <div class="icon-circle" style="left:686px;top:169px">
    <svg viewBox="0 0 36 36" fill="none" stroke="#fff" stroke-width="2"><rect x="9" y="5" width="18" height="26" rx="1"/><path d="M13 11h10M13 15h10M13 19h10M13 23h7"/></svg>
  </div>
  <div class="icon-circle" style="left:980px;top:169px">
    <svg viewBox="0 0 36 36" fill="none" stroke="#fff" stroke-width="2"><rect x="11" y="4" width="14" height="28" rx="2"/><path d="M16 7h4M17 28h2"/></svg>
  </div>

  <h3 class="feature-title" style="left:61px;top:255px;font-weight:400">Best Customer Services</h3>
  <h3 class="feature-title" style="left:338px;top:255px;font-weight:400">Save Money</h3>
  <h3 class="feature-title" style="left:595px;top:255px;font-weight:400">Cheaper Plans</h3>
  <h3 class="feature-title" style="left:889px;top:255px;font-weight:400">Talk More</h3>

  <ul class="ticks" style="left:71px;top:333px">
    <li>At vero eos et accusamus et iusto odio</li>
    <li>Praesentium voluptatum deleniti atque corrupti quos dolores et</li>
    <li>Excepturi sint occaecati cupiditate</li>
    <li>Sunt in culpa qui officia deserunt</li>
  </ul>
  <ul class="ticks" style="left:344px;top:333px">
    <li>At vero eos et accusamus et iusto odio</li>
    <li>Praesentium voluptatum deleniti atque corrupti quos dolores et</li>
    <li>Excepturi sint occaecati cupiditate</li>
    <li>Sunt in culpa qui officia deserunt</li>
  </ul>
  <ul class="ticks" style="left:615px;top:333px">
    <li>At vero eos et accusamus et iusto odio</li>
    <li>Praesentium voluptatum deleniti atque corrupti quos dolores et</li>
    <li>Excepturi sint occaecati cupiditate</li>
    <li>Sunt in culpa qui officia deserunt</li>
  </ul>
  <ul class="ticks" style="left:892px;top:333px">
    <li>At vero eos et accusamus et iusto odio</li>
    <li>Praesentium voluptatum deleniti atque corrupti quos dolores et</li>
    <li>Excepturi sint occaecati cupiditate</li>
    <li>Sunt in culpa qui officia deserunt</li>
  </ul>
</section>

<section class="cta faq" role="img" aria-label="Red tinted photo of a desk with a laptop behind the FAQ panel">
  <h3>Frequently Asked Questions</h3>
  <p>Sed ut perspiciatis unde omnis iste natus error sit voluptatem accusantium doloremque laudantium, totam rem aperiam, eaque ipsa quae ab illo inventore veritatis et quasi architecto</p>
  <a class="btn" style="background:var(--green)">Find Out More</a>
</section>

<section class="cta mobile" role="img" aria-label="Green tinted photo of mobile phones behind the plans panel">
  <h3>Mobile Phones &amp; Plans</h3>
  <p>Sed ut perspiciatis unde omnis iste natus error sit voluptatem accusantium doloremque laudantium, totam rem aperiam, eaque ipsa quae ab illo inventore veritatis et quasi architecto</p>
  <a class="btn" style="background:var(--red)">Find Out More</a>
</section>

<footer class="site-footer">
  <div class="brand">Quorvix</div>
  <nav class="footer-nav">
    <a style="left:267px">Home</a>
    <a style="left:334px">About Us</a>
    <a style="left:418px">Residential</a>
    <a style="left:511px">Support</a>
    <a style="left:589px">My Account</a>
  </nav>
  <p class="copyright">© 2018 Company Name | All Rights Reserved</p>
</footer>

</body>
</html>
```